Business Cards- The Manor at Brookridge Golf Club

We would like our business cards to look more high-end. We are a wedding venue that has been in business for 60+ years. We like our logo and our colors - primarily green and a touch of gold/beige. The owner wants our business cards to look more special..

Target Market(s)

Brides who have already toured our venue

Industry/Entity Type

Wedding venue - mansion

Contact Information for Business Card

Name, email, physical address, phone number

Colors
00AB8E
00BBA5
67D7C9
C6EFE9
E9F9F6

Requirements
Must have
• I think we would like our cards to be so pretty that people will want to keep them and will remember the venue. The venue is historic (built in 1850) and beautiful.
Nice to have
• Could we put an image of the building on one side and the contact info on the other?
Should not have
• The color black

```html
<!DOCTYPE html>
<html lang="en">
<head>
<meta charset="utf-8">
<title>The Manor at Brookridge Golf Club – Business Cards</title>
<link rel="stylesheet" href="https://fonts.googleapis.com/css2?family=Lato:wght@400;700&display=swap">
<style>
  :root {
    --venue-green: #7a9e4a;
    --venue-green-light: #8fb05e;
    --venue-beige: #d3c09f;
    --ink: #3a3a32;
    --card-white: #ffffff;
    --backdrop: #ecebe8;
  }
  * { box-sizing: border-box; margin: 0; padding: 0; }
  html, body {
    width: 1200px;
    height: 1181px;
    overflow: hidden;
    background: var(--backdrop);
    font-family: "Lato", sans-serif;
  }
  .canvas { position: relative; width: 1200px; height: 1181px; }
  .card {
    position: absolute;
    width: 654px;
    height: 404px;
    background: var(--card-white);
    box-shadow: 0 4px 18px rgba(60, 60, 50, 0.12);
    overflow: hidden;
  }
  .card--front { left: 179px; top: 164px; }
  .card--back { left: 480px; top: 627px; }

  .wordmark {
    position: absolute;
    inset: 0;
    display: flex;
    flex-direction: column;
    align-items: center;
    justify-content: center;
    color: var(--venue-green);
    font-weight: 700;
    text-align: center;
    line-height: 1.1;
  }
  .wordmark__main { font-size: 54px; letter-spacing: 1px; }
  .wordmark__sub { font-size: 22px; margin-top: 6px; letter-spacing: 0.5px; }

  .back-art { position: absolute; left: 0; top: 0; width: 654px; height: 404px; }

  .person {
    position: absolute;
    right: 26px;
    top: 196px;
    text-align: right;
  }
  .person__name { color: var(--venue-green); font-weight: 700; font-size: 24px; line-height: 1.2; }
  .person__role { color: var(--ink); font-size: 18px; margin-top: 2px; }

  .contact {
    position: absolute;
    right: 26px;
    top: 318px;
    list-style: none;
    text-align: right;
    color: var(--ink);
    font-size: 18px;
    line-height: 23.5px;
  }
  .contact li { display: flex; justify-content: flex-end; align-items: center; gap: 7px; }
  .contact svg { width: 14px; height: 14px; fill: var(--venue-green); flex: none; }

  .address {
    position: absolute;
    left: 26px;
    top: 340px;
    color: var(--ink);
    font-size: 18px;
    line-height: 23px;
    font-style: normal;
  }
</style>
</head>
<body>
<main class="canvas">

  <section class="card card--front" aria-label="Business card front">
    <div class="wordmark">
      <span class="wordmark__main">The Manor</span>
      <span class="wordmark__sub">at Brookridge Golf Club</span>
    </div>
  </section>

  <section class="card card--back" aria-label="Business card back">
    <svg class="back-art" viewBox="0 0 654 404" role="img" aria-label="Large decorative monogram flourish in green and beige">
      <defs>
        <linearGradient id="greenField" x1="0" y1="0" x2="1" y2="1">
          <stop offset="0" stop-color="var(--venue-green)"/>
          <stop offset="1" stop-color="var(--venue-green-light)"/>
        </linearGradient>
      </defs>
      <path d="M0 0 H654 V140 C560 170 470 150 420 190 C360 240 300 292 200 298 C110 302 30 285 0 262 Z"
            fill="url(#greenField)"/>
      <path d="M0 262 C30 285 110 302 200 298 C300 292 360 240 420 190 C470 150 560 170 654 140 V150 C565 178 478 160 428 198 C368 248 305 300 200 306 C105 310 28 292 0 272 Z"
            fill="var(--venue-beige)"/>
    </svg>

    <div class="person">
      <p class="person__name">Helen Whitfield</p>
      <p class="person__role">President - Owner</p>
    </div>

    <ul class="contact">
      <li>(401) 555-0148
        <svg viewBox="0 0 16 16" aria-hidden="true"><path d="M3 1h3l1 4-2 1c1 2 3 4 5 5l1-2 4 1v3c0 1-1 2-2 2C7 15 1 9 1 3c0-1 1-2 2-2z"/></svg>
      </li>
      <li>hwhitfield@brookridgegolf.com
        <svg viewBox="0 0 16 16" aria-hidden="true"><path d="M1 3h14v10H1z M2 4v1l6 4 6-4V4L8 8z" fill-rule="evenodd"/></svg>
      </li>
      <li>www.brookridgegolf.com
        <svg viewBox="0 0 16 16" aria-hidden="true"><circle cx="8" cy="8" r="7"/><path d="M8 1v14M1 8h14" stroke="#fff" stroke-width="1.2" fill="none"/></svg>
      </li>
    </ul>

    <address class="address">48 Alder Lane, Fairmont,<br>MD 21100</address>
  </section>

</main>
</body>
</html>
```